Inspiring Poster for Company Staff Room

What we need:
We want an awesome design to create a poster that will be plaque mounted in our staff room. We just went through a very motivating workshop to discover our "WHY" as a company...basically, to define the reason we are in business, and to define what motivates us to come to work every day. The poster must be motivating but really resonate with our team…we are not looking for a “typical” motivational poster that we can purchase off Amazon!

Who we are:
We are a property management company, a team of 20 that is passionate about our investors, and residents who rent from us, but more importantly, we love helping people and making a difference in our industry. We are proud and work hard for every single 5 star Google review we achieve.

Information for you:
We have included a mock up of the poster, which words we want, and the placement of them (in a general sense) but we need a designer to really bring this together in an inspiring poster that represents our company’s culture, feel, and fit. We have also included a logo file, as well as examples of our business cards, letterhead and thank you card already designed.
Here are the parameters:

(1) Poster size: 24” x 36”
(2) Full colour
(3) Must incorporate our company logo
(4) Must incorporate the following words:

Why do I come to work?

“To feel fulfilled by empathizing, educating and empowering our clients and co-workers so that we can build strong, impactful relationships”

Own the outcome

(5) Please see our website at www.brindlecovepm.com to get a feel for our company culture and for a better idea of our current company graphics

Target Market(s)

Our staff. Will not be seen by our clients

Industry/Entity Type

Real Estate

Font styles to use
Serif
Sans Serif

Requirements
Should not have
• Would not want this to be too "busy." if you can picture it, the poster will be mounted on the wall as soon as someone enters the room. The idea is to remind them each day why they come to work.

```html
<!DOCTYPE html>
<html lang="en">
<head>
<meta charset="utf-8">
<title>Why Do I Come To Work? – Staff Room Poster</title>
<link rel="stylesheet" href="https://fonts.googleapis.com/css2?family=Oswald:wght@400;500;700&family=Montserrat:wght@500&display=swap">
<style>
  :root {
    --brand-blue: #0b90cb;
    --ink: #3d3d3d;
    --paper: #ffffff;
    --backdrop: #232323;
  }
  html, body {
    margin: 0;
    padding: 0;
    width: 1050px;
    height: 1200px;
    overflow: hidden;
    background: var(--backdrop);
  }
  .stage {
    position: relative;
    width: 1050px;
    height: 1200px;
  }
  .poster {
    position: absolute;
    left: 125px;
    top: 37px;
    width: 800px;
    height: 1125px;
    display: block;
  }
  .frame-blue { fill: var(--brand-blue); }
  .frame-dark { fill: var(--ink); }
  .card { fill: var(--paper); }
  .tab { fill: var(--brand-blue); }
  .headline {
    font-family: 'Oswald', 'Arial Narrow', sans-serif;
  }
  .question { fill: var(--paper); font-weight: 700; font-size: 94px; }
  .lead { fill: var(--ink); font-weight: 400; font-size: 120px; }
  .verb-dark { fill: var(--ink); font-weight: 700; font-size: 200px; }
  .verb-light { fill: var(--paper); font-weight: 700; font-size: 170px; }
  .conjunction { fill: var(--paper); font-weight: 700; font-size: 137px; }
  .audience { fill: var(--brand-blue); font-weight: 400; font-size: 88px; }
  .bridge { fill: var(--ink); font-weight: 700; font-size: 75px; }
  .payoff-1 { fill: var(--paper); font-weight: 700; font-size: 225px; }
  .payoff-2 { fill: var(--paper); font-weight: 700; font-size: 163px; }
  .box-blue { fill: var(--brand-blue); stroke: var(--ink); stroke-width: 2; }
  .box-dark { fill: var(--ink); }
  .brand-mark { fill: var(--ink); }
  .brand-name { fill: var(--brand-blue); font-weight: 500; }
  .brand-name.primary { font-size: 62px; }
  .brand-name.secondary { font-size: 28px; }
  .rule { stroke: var(--brand-blue); stroke-width: 4; }
  .web {
    font-family: 'Montserrat', Arial, sans-serif;
    font-weight: 500;
    font-size: 26px;
    fill: var(--ink);
  }
</style>
</head>
<body>
<main class="stage">
  <svg class="poster" viewBox="0 0 1306 1836" xmlns="http://www.w3.org/2000/svg" aria-label="Why do I come to work? Staff room poster">
    <!-- border -->
    <rect class="frame-blue" x="0" y="0" width="1306" height="1836"/>
    <polygon class="frame-dark" points="0,1416 1306,846 1306,1836 0,1836"/>
    <rect class="card" x="26" y="24" width="1254" height="1788" rx="20"/>

    <!-- header tab -->
    <path class="tab" d="M76 24 L1231 24 L1166 116 Q1150 136 1126 136 L181 136 Q157 136 141 116 Z"/>
    <text class="headline question" x="196" y="111" textLength="915" lengthAdjust="spacingAndGlyphs">WHY DO I COME TO WORK?</text>

    <!-- statement -->
    <text class="headline lead" x="101" y="294" textLength="1095" lengthAdjust="spacingAndGlyphs">TO FEEL FULFILLED BY</text>
    <text class="headline verb-dark" x="112" y="476" textLength="1087" lengthAdjust="spacingAndGlyphs">EMPATHIZING</text>

    <rect class="box-blue" x="111" y="488" width="947" height="172"/>
    <text class="headline verb-light" x="124" y="652" textLength="920" lengthAdjust="spacingAndGlyphs">EDUCATING</text>
    <rect class="box-dark" x="1058" y="488" width="141" height="172"/>
    <g transform="translate(1128 574) rotate(90)">
      <text class="headline conjunction" x="0" y="50" text-anchor="middle" textLength="150" lengthAdjust="spacingAndGlyphs">AND</text>
    </g>

    <text class="headline verb-dark" x="112" y="836" textLength="1087" lengthAdjust="spacingAndGlyphs">EMPOWERING</text>
    <text class="headline audience" x="106" y="941" textLength="1072" lengthAdjust="spacingAndGlyphs">OUR CLIENTS &amp; CO-WORKERS</text>
    <text class="headline bridge" x="106" y="1026" textLength="1088" lengthAdjust="spacingAndGlyphs">SO THAT WE CAN BUILD STRONG,</text>

    <rect class="frame-blue" x="111" y="1053" width="1072" height="378"/>
    <text class="headline payoff-1" x="141" y="1256" textLength="1010" lengthAdjust="spacingAndGlyphs">IMPACTFUL</text>
    <text class="headline payoff-2" x="141" y="1411" textLength="1010" lengthAdjust="spacingAndGlyphs">RELATIONSHIPS</text>

    <!-- company name -->
    <rect class="brand-mark" x="150" y="1536" width="140" height="140"/>
    <text class="headline brand-name primary" x="366" y="1616" textLength="810" lengthAdjust="spacingAndGlyphs">BRINDLE COVE</text>
    <text class="headline brand-name secondary" x="401" y="1661" textLength="735" lengthAdjust="spacingAndGlyphs">PROPERTY MANAGEMENT</text>

    <!-- web address -->
    <line class="rule" x1="69" y1="1756" x2="233" y2="1756"/>
    <line class="rule" x1="1073" y1="1756" x2="1237" y2="1756"/>
    <text class="web" x="271" y="1765" textLength="765" lengthAdjust="spacingAndGlyphs">www.brindlecovepropertymanagement.com</text>
  </svg>
</main>
</body>
</html>
```